Flyer for American Indian Elders on Dementia Warning Signs

We need a flyer designed for older adults who are American Indian or Alaska Native (in the U.S.).

Ideally, the flyer should complement the colors of our logos. The project logo and our organization logo are attached to the brief.

When people see the flyer we want them to feel that it represents their culture, is warm, and professional but relatable to older adults and people who have limited incomes.

I have attached an earlier draft of the document we designed ourselves BUT we want different and better.

It is for older adults who have trouble reading so:
1. you must use a font that is 11.5 points or larger
2. Do not put text over complex pictures or use shading with words
3. You can use a serif font for the heading, but should use san serif for the body text
4. There should be good contrast between the font color and background

Please do not use any images that include a head dress or pictures of American Indian people or things that are very traditional or "token" imagery.

We need to save a small space under the call out box/ somewhere on the flyer for other people to add their logo once they download.

Let us know if you have questions or need additional information.

Target Market(s)

Older American Indian people

Font styles to use
Serif
Sans Serif

Requirements
Must have
• Easy to read for older adults
Should not have
• indian headdress

```html
<!DOCTYPE html>
<html lang="en">
<head>
<meta charset="utf-8">
<title>10 Signs of Thinking or Memory Changes That Might Be Dementia</title>
<link href="https://fonts.googleapis.com/css2?family=Bebas+Neue&family=Nunito:wght@400;600;700;800&display=swap" rel="stylesheet">
<style>
  :root {
    --teal: #3e7b7c;
    --teal-deep: #1e6a6c;
    --teal-bright: #3a9ea3;
    --clay: #b35a50;
    --sage: #a9bca7;
    --white: #ffffff;
    --grey: #a9a9a9;
    --rule: rgba(255,255,255,0.35);
  }
  * { box-sizing: border-box; margin: 0; padding: 0; }
  html, body { width: 848px; height: 1200px; overflow: hidden; background: var(--white); }
  body { font-family: "Nunito", sans-serif; color: var(--white); }
  .flyer { position: relative; width: 848px; height: 1200px; overflow: hidden; background: var(--white); }

  .backdrop { position: absolute; inset: 0; }
  .top-band { position: absolute; left: 0; top: 0; width: 848px; height: 12px; background: var(--clay); }

  .brand { position: absolute; left: 41px; top: 46px; display: flex; align-items: center; gap: 10px; }
  .brand-dot { width: 44px; height: 44px; border-radius: 50%; background: var(--teal-bright); }
  .brand-name { font-weight: 800; font-size: 13px; line-height: 14px; color: var(--teal-bright); white-space: nowrap; }

  .headline { position: absolute; left: 39px; top: 105px; display: flex; align-items: flex-start; }
  .headline-num { font-family: "Bebas Neue", sans-serif; font-size: 148px; line-height: 124px; color: var(--teal-deep); letter-spacing: -6px; }
  .headline-text { margin-left: 18px; margin-top: 14px; font-family: "Bebas Neue", sans-serif; font-size: 42px; line-height: 32px; color: var(--teal-deep); letter-spacing: -0.5px; white-space: nowrap; }

  .feathers { position: absolute; left: 460px; top: 50px; width: 90px; height: 128px;
    background: linear-gradient(90deg, #9fd0d6 0%, #8cc46a 50%, #c86d64 100%); opacity: 0.55; border-radius: 45px 45px 10px 10px; }

  .callout { position: absolute; left: 578px; top: 12px; width: 229px; height: 286px; background: var(--clay);
    border-bottom: 7px solid var(--teal-deep); padding: 34px 0 0 25px; }
  .callout p { font-size: 14.6px; line-height: 21.4px; font-weight: 600; white-space: nowrap; }

  .intro { position: absolute; left: 41px; top: 253px; width: 497px; height: 72px; background: var(--white);
    border: 1.5px solid var(--teal); padding: 9px 0 0 16px; }
  .intro p { font-size: 13.8px; line-height: 17.2px; font-weight: 800; color: var(--teal-deep); white-space: nowrap; }

  .col-rule { position: absolute; width: 1px; background: var(--rule); }
  .row-rule { position: absolute; height: 1px; background: var(--rule); }

  .sign { position: absolute; font-size: 16px; line-height: 22.8px; white-space: nowrap; }
  .sign-num { position: absolute; left: -21px; top: -3px; font-family: "Bebas Neue", sans-serif; font-size: 25px; line-height: 26px; }
  .sign-lead { font-weight: 800; letter-spacing: 0.2px; }
  .sign-list { list-style: none; }
  .sign-list li { position: relative; font-weight: 400; letter-spacing: 0.3px; }
  .sign-list li::before { content: ""; position: absolute; left: -16px; top: 6px; width: 7px; height: 7px;
    border-top: 1.5px solid var(--white); border-right: 1.5px solid var(--white); transform: rotate(45deg); }

  .main-points { position: absolute; left: 580px; top: 553px; width: 228px; height: 505px; }
  .main-points svg { position: absolute; inset: 0; }
  .main-points-title { position: absolute; top: 586px; left: 580px; width: 228px; text-align: center;
    font-family: "Bebas Neue", sans-serif; font-size: 47px; line-height: 48px; color: var(--teal-deep); letter-spacing: -0.5px; }
  .point { position: absolute; left: 580px; width: 228px; text-align: center; font-size: 14.2px; line-height: 17.2px;
    font-weight: 800; color: var(--teal); white-space: nowrap; }

  .footer-note { position: absolute; left: 41px; top: 1131px; width: 497px; height: 69px; background: var(--clay); padding: 9px 0 0 9px; }
  .footer-note p { font-size: 14.4px; line-height: 17.3px; white-space: nowrap; }
  .footer-note strong { font-weight: 800; }

  .partner-logo-space { position: absolute; left: 653px; top: 1121px; font-family: "Bebas Neue", sans-serif; font-size: 44px; line-height: 40px; color: var(--grey); }
</style>
</head>
<body>
<div class="flyer">
  <svg class="backdrop" width="848" height="1200" viewBox="0 0 848 1200" aria-hidden="true">
    <polygon points="0,342 848,104 848,1050 533,1124 533,1200 0,1200" fill="var(--teal)"/>
  </svg>
  <div class="top-band"></div>

  <div class="brand">
    <span class="brand-dot"></span>
    <span class="brand-name">CEDAR CIRCLE CENTER<br>FOR ELDER BRAIN HEALTH</span>
  </div>

  <div class="headline">
    <div class="headline-num">10</div>
    <h1 class="headline-text">SIGNS OF THINKING OR<br>MEMORY CHANGES THAT<br>MIGHT BE DEMENTIA</h1>
  </div>

  <div class="feathers" role="img" aria-label="Illustration of three feathers in blue, green and red"></div>

  <div class="callout">
    <p>As we get older, we may<br>slow down a bit. This is<br>a normal part of aging.<br>Changes in memory or<br>thinking that make it<br>harder to get through<br>the day, are not a normal<br>part of aging. These<br>may be early signs of<br>dementia.</p>
  </div>

  <div class="intro">
    <p>Because american indian and alaska native people have a high<br>risk of dementia, it is important to know the warning signs. do<br>you have any of these 10 signs? if so, talk to your doctor.</p>
  </div>

  <div class="col-rule" style="left:289px; top:346px; height:778px;"></div>
  <div class="col-rule" style="left:557px; top:346px; height:778px;"></div>
  <div class="row-rule" style="left:0; top:540px; width:285px;"></div>
  <div class="row-rule" style="left:0; top:698px; width:285px;"></div>
  <div class="row-rule" style="left:0; top:794px; width:285px;"></div>
  <div class="row-rule" style="left:0; top:926px; width:285px;"></div>
  <div class="row-rule" style="left:293px; top:540px; width:262px;"></div>
  <div class="row-rule" style="left:291px; top:698px; width:264px;"></div>
  <div class="row-rule" style="left:297px; top:881px; width:258px;"></div>

  <div class="sign" style="left:61px; top:346px;">
    <span class="sign-num">1.</span>
    <p class="sign-lead">Memory loss that affects<br>your daily life. You may:</p>
    <ul class="sign-list"><li>Forget events or import-<br>ant dates</li><li>Repeat yourself</li><li>Rely more often on lists or<br>sticky notes<br>to remember things</li></ul>
  </div>

  <div class="sign" style="left:66px; top:551px;">
    <span class="sign-num" style="left:-26px;">2.</span>
    <p class="sign-lead">Trouble planning or<br>solving problems. You<br>may have a harder time:</p>
    <ul class="sign-list" style="margin-left:-5px;"><li>Paying bills</li><li>Cooking recipes you have<br>used for years</li></ul>
  </div>

  <div class="sign" style="left:61px; top:711px;">
    <span class="sign-num">3.</span>
    <p class="sign-lead">Get confused about the<br>time, date, or where you<br>are.</p>
  </div>

  <div class="sign" style="left:61px; top:802px;">
    <span class="sign-num">4.</span>
    <p class="sign-lead">Daily tasks are getting<br>harder, including:</p>
    <ul class="sign-list"><li>Driving</li><li>Making a grocery list or<br>going shopping</li></ul>
  </div>

  <div class="sign" style="left:61px; top:939px;">
    <span class="sign-num">5.</span>
    <p class="sign-lead">Trouble with how your<br>eyesight and thinking<br>work together that gets<br>worse. This includes:</p>
    <ul class="sign-list"><li>Tripping, falls, or prob-<br>lems with your balance</li><li>Spilling or dropping<br>things more</li></ul>
  </div>

  <div class="sign" style="left:330px; top:346px;">
    <span class="sign-num">6.</span>
    <p class="sign-lead">New trouble talking or<br>writing. You have a hard<br>time finding the words<br>you want to say. For<br>example, you may say<br>“that thing on your wrist<br>that tells time” instead of<br>“watch.”</p>
  </div>

  <div class="sign" style="left:330px; top:551px;">
    <span class="sign-num">7.</span>
    <p class="sign-lead">Lose and cannot find<br>things. For example, you:</p>
    <ul class="sign-list"><li>Can’t find the coffee pot<br>that you use every day</li><li>Might put your car keys in<br>the freezer</li></ul>
  </div>

  <div class="sign" style="left:330px; top:711px;">
    <span class="sign-num">8.</span>
    <p class="sign-lead">Notice changes in mood<br>or personality, such as<br>being:</p>
    <ul class="sign-list"><li>Easily mad or sad in ev-<br>eryday situations</li><li>More fearful (scared) or<br>suspicious (not trusting)</li></ul>
  </div>

  <div class="sign" style="left:330px; top:893px;">
    <span class="sign-num">9.</span>
    <p class="sign-lead">Act different and make<br>poor choices. This may<br>make you more likely to:</p>
    <ul class="sign-list"><li>Spend money you do not<br>have or be a scam victim</li><li>Stop washing up regularly<br>or pay less<br>attention to how you look</li><li>Forget to take care<br>of your pet</li></ul>
  </div>

  <div class="sign" style="left:604px; top:346px;">
    <span class="sign-num" style="left:-23px;">10.</span>
    <p class="sign-lead">Pull away from friends<br>and family because it<br>is harder to keep up.<br>You may not want to do<br>things you used to en-<br>joy, like sporting events,<br>church, music, or sex.</p>
  </div>

  <div class="main-points" aria-hidden="true">
    <svg width="228" height="505" viewBox="0 0 228 505">
      <polygon points="24,0 204,0 228,24 228,481 204,505 24,505 0,481 0,24" fill="var(--sage)"/>
      <polygon points="26,3 202,3 225,26 225,479 202,502 26,502 3,479 3,26" fill="none" stroke="#c9d6c6" stroke-width="1" stroke-dasharray="2 2"/>
      <polyline points="38,89 114,97 190,89" fill="none" stroke="#ffffff" stroke-width="1" stroke-dasharray="1.5 1.5"/>
      <polyline points="38,480 114,476 190,480" fill="none" stroke="#ffffff" stroke-width="1" stroke-dasharray="1.5 1.5"/>
    </svg>
  </div>
  <h2 class="main-points-title">MAIN POINTS</h2>
  <p class="point" style="top:674px;">American Indian and<br>Alaska Native people have<br>a high risk of dementia.</p>
  <p class="point" style="top:743px;">Big changes in memory or<br>thinking that make it hard<br>to get through the day are<br>not a normal part of aging.</p>
  <p class="point" style="top:829px;">People with one or more<br>of these 10 signs should<br>talk to their doctor to<br>find the cause. It is not<br>always dementia.</p>
  <p class="point" style="top:931px;">Early dementia<br>diagnosis gives you a<br>chance to get care and<br>plan your future.</p>

  <div class="footer-note">
    <p>To learn more about the warning signs of dementia in American<br>Indian and Alaska Native people, visit: <strong>www.CedarCircleElders.org,</strong><br><strong>www.healthyagingnow.org</strong></p>
  </div>

  <div class="partner-logo-space">LOGO HERE</div>
</div>
</body>
</html>
```